Need a tea box packaging design

* Organic Herbal tea
* Imported from india to france for european community
* our main rivals are " ZENDRA" tea and " BRAVO" tea.
* the product will be sold online and shops.
* 15 variety of teas will be imported.
* The details in the attached file.
The Packaging contents:
Main page :
Brand Name : KORIL ( logo attached)
Name of the product: KELORA THE NOIR ( which means Kelora black tea)
Type of the product : Infusion
No of tea bags : 20
Weight of each bag : 1,5 gm
Total weight : 30 gm
Organic label name : Europe ( organic logo attached)
vegan label : vegan ( vegan label attached)
The other side contents will be given later.
A model that i have designed with another designer is attached. It is nice. But i am expecting more than that. ( attached)
Some designs that i like are attached here.
As mentionned earlier there will 15 variety of teas, so the design should easily modifiable by just changing colours.
Updates
Project Deadline Extended Reason: I think the deadline is very short due to the weekend. So, I feel it is better to extend the deadline by 5 days. Added Saturday, January 21, 2017
Target Market(s)
Europe. Mainly france.
Industry/Entity Type
Community
Requirements
Must have
- * Design should be modern and colourfull.
- * I like pattern works, Vectorials
- * Yoga silouhaites in the design is appreciable.
- * The design should express wellness, joy and love
Nice to have
- "Zendra" tea in my inspirational design.
- * The ingredients can be showed in vectorial designs in the back ground.
- * The end user must see the box while taking the tea and appreciate
- * The end user must search and find some hidden things.
- * The box must be communicative.
- * Trendy frames.
Should not have
- No need to have tea cups

```html
<!DOCTYPE html>
<html lang="en">
<head>
<meta charset="utf-8">
<title>KORIL – Kelora The Noir Infusion</title>
<link rel="stylesheet" href="https://fonts.googleapis.com/css2?family=Oswald:wght@300;400;600;700&family=Open+Sans:wght@400;600&display=swap">
<style>
  :root {
    --stage: #cfcfcf;
    --face-bg: #eef0df;
    --pattern-tone: #d6dcb4;
    --label-fill: #8ba83b;
    --label-top: #82a035;
    --label-border: #34410f;
    --ink-dark: #27300c;
    --ribbon: #2c3510;
    --ribbon-text: #a9c45a;
    --band: #6a1c16;
    --cream: #f3f0d8;
    --soft-text: #eef2c8;
    --badge: #9dba4d;
  }
  * { margin: 0; padding: 0; box-sizing: border-box; }
  html, body { width: 1200px; height: 1200px; overflow: hidden; }
  body { background: var(--stage); font-family: "Open Sans", sans-serif; position: relative; }

  .box-face {
    position: absolute; left: 260px; top: 40px;
    width: 680px; height: 1120px;
    background: var(--face-bg);
    overflow: hidden;
  }
  .pattern-field {
    position: absolute; inset: 0;
    background: radial-gradient(circle at 30% 25%, var(--pattern-tone), var(--face-bg) 60%),
                radial-gradient(circle at 75% 80%, var(--pattern-tone), transparent 55%);
  }
  .face-frame {
    position: absolute; inset: 22px;
    border: 1.5px solid #b9bea2;
  }

  .label { position: absolute; left: 110px; top: 115px; width: 460px; height: 840px; }
  .label-shape { position: absolute; inset: 0; }
  .herb-backdrop {
    position: absolute; left: 10px; top: 300px; width: 440px; height: 260px;
    background: radial-gradient(ellipse at center, #a3bf55, transparent 70%);
  }

  .brand {
    position: absolute; top: 70px; left: 0; right: 0;
    text-align: center; color: #fff;
    font-family: "Oswald", sans-serif; font-weight: 300;
    font-size: 92px; letter-spacing: 6px; line-height: 1;
  }
  .divider { position: absolute; left: 6px; right: 6px; top: 260px; height: 3px; background: #a6c25a; }
  .stars {
    position: absolute; top: 272px; left: 0; right: 0; text-align: center;
    color: var(--ink-dark); font-size: 16px; letter-spacing: 10px;
  }
  .product-name {
    position: absolute; top: 292px; left: 0; right: 0; text-align: center;
    font-family: "Oswald", sans-serif; font-weight: 700;
    font-size: 140px; line-height: 1; color: var(--ink-dark); letter-spacing: -2px;
  }
  .product-sub {
    position: absolute; top: 455px; left: 40px; right: 40px;
    display: flex; align-items: center; gap: 14px;
    font-family: "Oswald", sans-serif; font-weight: 400;
    font-size: 38px; color: var(--ink-dark); line-height: 1;
  }
  .product-sub::before, .product-sub::after { content: ""; flex: 1; height: 5px; background: var(--ink-dark); }

  .ribbon { position: absolute; top: 505px; left: 40px; right: 40px; height: 60px; }
  .ribbon-tail { position: absolute; top: 14px; height: 38px; width: 120px; background: var(--ribbon); }
  .ribbon-tail.left { left: 0; clip-path: polygon(0 0, 100% 0, 100% 100%, 0 100%, 14px 50%); }
  .ribbon-tail.right { right: 0; clip-path: polygon(0 0, 100% 0, calc(100% - 14px) 50%, 100% 100%, 0 100%); }
  .ribbon-center {
    position: absolute; left: 90px; right: 90px; top: 0; height: 60px;
    background: var(--ribbon); border: 2px solid #5f7424;
    display: flex; align-items: center; justify-content: center;
    font-family: "Oswald", sans-serif; font-weight: 300;
    font-size: 36px; color: var(--ribbon-text); letter-spacing: 1px;
  }

  .type-band {
    position: absolute; top: 575px; left: 2px; right: 2px; height: 46px;
    background: var(--band);
    display: flex; align-items: center; justify-content: center; gap: 14px;
    font-family: "Oswald", sans-serif; font-weight: 400;
    font-size: 36px; letter-spacing: 9px; color: var(--cream);
  }
  .type-band .rule { width: 60px; height: 2px; background: var(--cream); }

  .weight { position: absolute; font-size: 19px; color: var(--soft-text); }
  .weight.each { left: 20px; top: 670px; }
  .weight.total { right: 18px; top: 636px; }

  .bag-count { position: absolute; left: 30px; top: 728px; display: flex; align-items: center; gap: 4px; }
  .bag-count .num {
    font-family: "Oswald", sans-serif; font-weight: 600; font-size: 40px;
    color: var(--ink-dark); line-height: 0.9;
  }
  .bag-count .num small { display: block; font-size: 17px; font-weight: 400; }

  .cert { position: absolute; top: 700px; width: 84px; height: 84px; border-radius: 50%; background: var(--badge); }
  .cert.vegan { left: 186px; }
  .cert.organic { left: 320px; }
</style>
</head>
<body>
  <main class="box-face">
    <div class="pattern-field" role="img" aria-label="Light green mandala and paisley line pattern with faint yoga pose silhouettes"></div>
    <div class="face-frame"></div>

    <section class="label">
      <svg class="label-shape" viewBox="0 0 460 840" width="460" height="840" aria-hidden="true">
        <polygon points="0,70 60,40 230,0 400,40 460,70 460,770 400,800 230,840 60,800 0,770"
                 fill="var(--label-fill)" stroke="var(--label-border)" stroke-width="6"/>
        <polygon points="4,72 61,44 230,5 399,44 456,72 456,258 4,258" fill="var(--label-top)"/>
      </svg>
      <div class="herb-backdrop" role="img" aria-label="Soft illustration of tea herb leaves and flower spikes"></div>

      <div class="brand">KORIL</div>
      <div class="divider"></div>
      <div class="stars">★ ★ ● ★ ★</div>
      <h1 class="product-name">KELORA</h1>
      <div class="product-sub">THE NOIR</div>

      <div class="ribbon">
        <div class="ribbon-tail left"></div>
        <div class="ribbon-tail right"></div>
        <div class="ribbon-center">PREMIUM</div>
      </div>

      <div class="type-band"><span class="rule"></span>INFUSION<span class="rule"></span></div>

      <p class="weight each">Each bag : 1.5 gm</p>
      <p class="weight total">Total weight : 30 gm</p>

      <div class="bag-count">
        <div class="num">20<small>Bags</small></div>
        <svg width="48" height="40" viewBox="0 0 48 40" aria-hidden="true">
          <path d="M4 6 h30 v14 a15 15 0 0 1 -30 0 z" fill="var(--ink-dark)"/>
          <path d="M34 10 h5 a6 6 0 0 1 0 12 h-5" fill="none" stroke="var(--ink-dark)" stroke-width="3"/>
          <rect x="0" y="35" width="40" height="3" fill="var(--ink-dark)"/>
        </svg>
      </div>

      <div class="cert vegan" role="img" aria-label="Vegan certification badge"></div>
      <div class="cert organic" role="img" aria-label="European organic certification badge"></div>
    </section>
  </main>
</body>
</html>
```